political campaign lawn sign - Governor's Council in Massachuesetts

We are looking for a political lawn sign. We are running a campaign for Governor's Council in Massachusetts. This sign will be on the lawn of homes and businesses so people driving by will see it. It needs to be simple and bold. The last name is long so maybe it could say vote for Marty and then Kolbeck will be big a bold on the next line??
We need it to say:
Vote for Martin Kolbeck
Governor's Council.

Target Market(s)

local residents

Industry/Entity Type

Politcal Campaign

Font styles to use
Sans Serif
Other font styles liked:
• not sure what font but a modern looking one such as Helvetica, Arial, Sans Seri, sharp sans..

Colors
0054AA
0677BA
7BADD7
CADEEF
E8F1F8
00AB8E
00BBA5
67D7C9
C6EFE9
E9F9F6
FFF300
FFF600
FEFA6F
FFFEC7
FFFEE8

Requirements
Must have
• My name written out with a Capital D and R but lower case for every other letter so its Marty Kolbeck
Nice to have
• modern font , the Colors of the lawn sign should have Blue, Yellow and White something bold that will stand out
Should not have
• any maps of Massachusetts

```html
<!DOCTYPE html>
<html lang="en">
<head>
<meta charset="utf-8">
<title>Vote for Marty Kolbeck – Governor's Council Lawn Sign</title>
<link rel="stylesheet" href="https://fonts.googleapis.com/css2?family=Montserrat:wght@400;700;800&display=swap">
<style>
  :root {
    --backdrop: #c8c8c8;
    --campaign-blue: #0054AA;
    --campaign-yellow: #FFF600;
    --campaign-white: #FFFFFF;
    --accent-teal: #00AB8E;
    --accent-mint: #67D7C9;
    --portrait-light: #c7a08c;
    --portrait-mid: #6b5a55;
    --portrait-dark: #1e2434;
  }
  html, body {
    margin: 0;
    padding: 0;
    width: 1200px;
    height: 2506px;
    overflow: hidden;
    background: var(--backdrop);
  }
  .canvas {
    position: relative;
    width: 1200px;
    height: 2506px;
  }
  .lawn-sign {
    position: absolute;
    left: 100px;
    top: 586px;
    width: 1000px;
    height: 1332px;
    box-shadow: 18px 22px 28px rgba(0,0,0,0.35);
  }
  .lawn-sign svg { display: block; width: 100%; height: 100%; }
  .sign-text { font-family: 'Montserrat', Arial, sans-serif; }
  .headline-kicker { fill: var(--campaign-yellow); font-weight: 800; font-size: 75px; }
  .headline-name { fill: var(--campaign-white); font-weight: 800; font-size: 206px; letter-spacing: -4px; }
  .surname { fill: var(--accent-mint); font-weight: 800; font-size: 76px; }
  .office { fill: var(--campaign-white); font-weight: 700; font-size: 36px; }
  .web-address { fill: var(--campaign-white); font-weight: 700; font-size: 33px; }
  .web-address .domain-suffix { font-weight: 400; }
</style>
</head>
<body>
<main class="canvas">
  <section class="lawn-sign" aria-label="Campaign lawn sign: Vote for Marty Kolbeck, Governor's Council">
    <svg viewBox="0 0 808 1076" xmlns="http://www.w3.org/2000/svg">
      <defs>
        <linearGradient id="portraitTone" x1="0" y1="0" x2="0" y2="1">
          <stop offset="0" stop-color="var(--portrait-light)"/>
          <stop offset="0.55" stop-color="var(--portrait-mid)"/>
          <stop offset="1" stop-color="var(--portrait-dark)"/>
        </linearGradient>
      </defs>

      <!-- colour fields -->
      <rect class="field-yellow" width="808" height="1076" fill="var(--campaign-yellow)"/>
      <polygon class="field-blue" points="0,0 808,0 808,637 0,395" fill="var(--campaign-blue)"/>
      <polygon class="field-white" points="0,395 499,545 0,717" fill="var(--campaign-white)"/>

      <!-- candidate portrait area -->
      <path class="candidate-portrait" role="img" aria-label="Portrait photo of the candidate in a dark suit and tie"
            d="M245,575 Q245,450 375,450 Q505,450 505,575 L505,780 Q700,825 808,880 L808,1076 L58,1076 Q70,865 245,795 Z"
            fill="url(#portraitTone)"/>

      <!-- headline -->
      <text class="sign-text headline-kicker" x="88" y="108">VOTE FOR</text>
      <text class="sign-text headline-name" x="82" y="280">Marty</text>
      <text class="sign-text surname" x="718" y="392" text-anchor="end">Kolbeck</text>
      <text class="sign-text office" x="718" y="432" text-anchor="end">Governor's Council</text>

      <!-- web address band -->
      <polygon class="web-band" points="426,992 808,992 808,1049 398,1049" fill="var(--accent-teal)"/>
      <text class="sign-text web-address" x="760" y="1033" text-anchor="end">kolbeckforcouncil<tspan class="domain-suffix">.net</tspan></text>
    </svg>
  </section>
</main>
</body>
</html>
```